Bobcat / excavator / tipper contractor
info for back of card {
2.3 ton bobcat 1.6m wide
3.6 ton excavator 1.6 wide
4.5M tipper 2.4 wide }
In the industry since 1999
Experienced in all aspects of bobcat excavator general hire work
Brisbane to goldcoast area
competitive rates

As for the image uploaded, I kind of like the H made out of the bulidings and the brown and yellow are the colors of my footy team. but open to anything that is unique the portrays excavation that can become a symbol for my business.so the H is good or something with DMR.

Im wanting to create business cards and either large magnets or a wrap for the front of the truck.
dresfordmachinerental @ examplemail . test

Contractor

Luke Dresford
Dresford Machine Rental Pty Ltd
ABN 51830296714
mobile 0491326048
dresfordmachinerental@examplemail.test

```html
<!DOCTYPE html>
<html lang="en">
<head>
<meta charset="utf-8">
<title>Dresford Machine Rental – Business Cards</title>
<link href="https://fonts.googleapis.com/css2?family=Open+Sans:wght@400;600&display=swap" rel="stylesheet">
<style>
  :root {
    --brown: #a2410f;
    --brown-dark: #7a2e08;
    --yellow: #d4d21f;
    --white: #ffffff;
    --paper: #f4f4f2;
    --backdrop: #e8e3da;
    --ink-brown: #9a3e12;
  }
  * { box-sizing: border-box; margin: 0; padding: 0; }
  html, body {
    width: 1200px; height: 892px; overflow: hidden;
    background: var(--backdrop);
    font-family: "Open Sans", Arial, sans-serif;
  }
  .stage {
    position: relative; width: 1200px; height: 892px;
    display: flex; align-items: center; justify-content: center; gap: 110px;
  }
  .card {
    position: relative; width: 400px; height: 655px;
    background: var(--white);
    box-shadow: 0 10px 30px rgba(60,40,20,.25);
    overflow: hidden;
  }

  /* Front */
  .front-panel {
    position: absolute; inset: 0 0 auto 0; height: 330px;
    background: linear-gradient(135deg, var(--brown) 0%, var(--brown-dark) 100%);
    color: var(--white);
    padding: 54px 40px 0 46px;
  }
  .person-name { font-size: 40px; font-weight: 400; line-height: 1.1; letter-spacing: .3px; }
  .person-role { font-size: 22px; font-weight: 400; margin-top: 4px; }
  .abn { font-size: 19px; margin-top: 30px; }
  .contact-list { list-style: none; margin-top: 30px; }
  .contact-list li {
    display: flex; align-items: center; gap: 12px;
    font-size: 17px; margin-bottom: 8px; white-space: nowrap;
  }
  .contact-list svg { width: 17px; height: 17px; flex: none; }
  .contact-list .email { font-size: 15px; }

  .front-brand {
    position: absolute; top: 330px; left: 0; right: 0; height: 240px;
    display: flex; flex-direction: column; align-items: center; justify-content: center; gap: 18px;
    background: var(--paper);
  }
  .brand-square { width: 46px; height: 46px; background: var(--ink-brown); }
  .brand-name {
    color: var(--ink-brown); font-weight: 600; font-size: 25px; letter-spacing: .5px; text-align: center;
  }
  .front-tab {
    position: absolute; left: 40px; right: 40px; bottom: 0; height: 46px;
    background: var(--brown); border-radius: 10px 10px 0 0;
  }

  /* Back */
  .card--back { border: 8px solid var(--yellow); background: var(--paper); }
  .back-brand {
    position: absolute; inset: 0;
    display: flex; flex-direction: column; align-items: center; justify-content: center; gap: 34px;
  }
  .back-brand .brand-square { width: 80px; height: 80px; }
  .back-brand .brand-name { font-size: 31px; line-height: 1.3; }
</style>
</head>
<body>
<main class="stage">
  <article class="card card--front">
    <section class="front-panel">
      <h1 class="person-name">Luke Dresford</h1>
      <p class="person-role">Director</p>
      <p class="abn">ABN 51830296714</p>
      <ul class="contact-list">
        <li>
          <svg viewBox="0 0 16 16" aria-hidden="true"><rect width="16" height="16" rx="2" fill="#fff"/><path d="M5 3.5l2 2-1.2 1.3a7 7 0 0 0 3.4 3.4L10.5 9l2 2-1.5 1.5C7 12 4 9 3.5 5z" fill="#a2410f"/></svg>
          <span>0491326048</span>
        </li>
        <li class="email">
          <svg viewBox="0 0 16 16" aria-hidden="true"><rect width="16" height="16" rx="2" fill="#fff"/><rect x="3" y="4.5" width="10" height="7" fill="none" stroke="#a2410f" stroke-width="1.2"/><path d="M3 4.5l5 4 5-4" fill="none" stroke="#a2410f" stroke-width="1.2"/></svg>
          <span>dresfordmachinerental@examplemail.test</span>
        </li>
      </ul>
    </section>
    <section class="front-brand">
      <span class="brand-square" aria-hidden="true"></span>
      <p class="brand-name">Dresford Machine Rental</p>
    </section>
    <div class="front-tab" aria-hidden="true"></div>
  </article>

  <article class="card card--back">
    <section class="back-brand">
      <span class="brand-square" aria-hidden="true"></span>
      <p class="brand-name">Dresford<br>Machine Rental</p>
    </section>
  </article>
</main>
</body>
</html>
```